Torvel, Inc. new buisness cards - brand guide included

We need new business cards. SLEAK SIMPLE FINANCE. They must include a place for NAME, TITLE, CELL, OFFICE PHONE, EMAIL. they also must include our services across the bottom. AIR, OCEAN, FTL, LTL, EXPRESS. for reference this will be being handed to some of the most prestigious shipping companies in a america.

Target Market(s)

Finance and corporate

Contact Information for Business Card

We need new business cards. SLEAK SIMPLE FINANCE. They must include a place for NAME, TITLE, CELL, OFFICE PHONE, EMAIL. they also must include our services across the bottom. AIR, OCEAN, FTL, LTL, EXPRESS.

Requirements
Must have
• We need new business cards. SLEAK SIMPLE FINANCE. They must include a place for NAME, TITLE, CELL, OFFICE PHONE, EMAIL. they also must include our services across the bottom. AIR, OCEAN, FTL, LTL, EXPRESS.
Nice to have
• USE THE COLORS AND LOGO IN THE BRAND GUIDE :)

```html
<!DOCTYPE html>
<html lang="en">
<head>
<meta charset="utf-8">
<title>Torvel, Inc. Business Cards</title>
<link rel="stylesheet" href="https://fonts.googleapis.com/css2?family=Open+Sans:wght@400;600;700&display=swap">
<style>
  :root {
    --backdrop: #e6e6e4;
    --card-dark: #2a2a2a;
    --card-edge: #3a3a3a;
    --band-light: #ebe9e4;
    --ink-dark: #262626;
    --ink-mid: #4a4a4a;
    --ink-light: #f1efe9;
    --ink-soft: #a9a9a9;
    --mark-grey: #616161;
    --rule-grey: #8a8a8a;
  }
  * { box-sizing: border-box; margin: 0; padding: 0; }
  html, body {
    width: 1200px; height: 801px; overflow: hidden;
    background: var(--backdrop);
    font-family: "Open Sans", Arial, sans-serif;
  }
  .sheet {
    position: relative; width: 1200px; height: 801px;
    display: flex; align-items: center; justify-content: center; gap: 36px;
  }
  .card {
    position: relative; width: 540px; height: 309px;
    background: var(--card-dark);
    box-shadow: 0 10px 24px rgba(0,0,0,.22);
    overflow: hidden;
  }

  /* Front */
  .card-front__brand {
    height: 160px; display: flex; align-items: center; justify-content: center; gap: 14px;
  }
  .brand-square { width: 22px; height: 22px; background: var(--ink-light); }
  .brand-name { color: var(--ink-light); font-size: 40px; font-weight: 600; letter-spacing: 1px; }
  .card-front__band {
    height: 106px; background: var(--band-light);
    display: flex; align-items: center; justify-content: center;
  }
  .person { text-align: right; padding-right: 18px; }
  .person__name { color: var(--ink-dark); font-size: 19px; font-weight: 700; letter-spacing: .5px; }
  .person__title { color: var(--ink-mid); font-size: 14px; }
  .band-divider { width: 1px; height: 78px; background: var(--ink-mid); }
  .contacts { list-style: none; padding-left: 16px; }
  .contacts li {
    display: flex; align-items: center; gap: 7px;
    color: var(--ink-dark); font-size: 14px; line-height: 19px;
  }
  .contacts svg { width: 12px; height: 12px; fill: var(--ink-dark); flex: none; }
  .card-front__address {
    height: 43px; display: flex; align-items: center; justify-content: center;
    color: var(--ink-soft); font-size: 14px; letter-spacing: .3px;
  }

  /* Back */
  .card-back { border: 3px solid var(--card-edge); }
  .card-back__mark {
    position: absolute; top: 62px; left: 0; right: 0; text-align: center;
    color: var(--mark-grey); font-size: 76px; font-weight: 600; letter-spacing: 1px; line-height: 1;
    white-space: nowrap;
  }
  .services { position: absolute; left: 40px; right: 40px; top: 196px; }
  .services__rule { display: flex; align-items: center; }
  .services__rule::before, .services__rule::after {
    content: ""; flex: 1; height: 1px; background: var(--rule-grey);
  }
  .services__label {
    background: var(--ink-light); color: var(--ink-dark);
    font-size: 13px; font-weight: 700; letter-spacing: .5px;
    padding: 2px 14px; border-radius: 12px; margin: 0 6px;
  }
  .services__list {
    list-style: none; display: flex; justify-content: center; gap: 12px; margin-top: 12px;
    color: var(--ink-light); font-size: 17px; letter-spacing: .5px;
  }
  .services__list li::before { content: "\2022"; margin-right: 6px; }
</style>
</head>
<body>
<main class="sheet">

  <section class="card card-front" aria-label="Business card front">
    <div class="card-front__brand">
      <span class="brand-square"></span>
      <span class="brand-name">Torvel, Inc.</span>
    </div>
    <div class="card-front__band">
      <div class="person">
        <p class="person__name">DANIEL REYES</p>
        <p class="person__title">Executive Director</p>
      </div>
      <span class="band-divider"></span>
      <ul class="contacts">
        <li><svg viewBox="0 0 12 12" aria-hidden="true"><path d="M1 4c0-2 2-3 5-3s5 1 5 3l-2 1-1-2H4L3 5zM3 6h6l1 5H2z"/></svg>055-310 482 617</li>
        <li><svg viewBox="0 0 12 12" aria-hidden="true"><path d="M3 0h6v12H3zM4 1v9h4V1z"/></svg>055-310 482 618</li>
        <li><svg viewBox="0 0 12 12" aria-hidden="true"><path d="M0 2h12v8H0zM1 3l5 4 5-4z"/></svg>hello@torvelco.com</li>
        <li><svg viewBox="0 0 12 12" aria-hidden="true"><circle cx="6" cy="6" r="6"/></svg>www.torvelfreight.com</li>
      </ul>
    </div>
    <p class="card-front__address">18 Harbor Lane, Dunmore, OH 44012</p>
  </section>

  <section class="card card-back" aria-label="Business card back">
    <p class="card-back__mark">Torvel, Inc.</p>
    <div class="services">
      <div class="services__rule"><span class="services__label">OUR SERVICES</span></div>
      <ul class="services__list">
        <li>AIR</li><li>OCEAN</li><li>FTL</li><li>LTL</li><li>EXPRESS</li>
      </ul>
    </div>
  </section>

</main>
</body>
</html>
```